Business card for a gourmet fruit and vegetable retail store

Please design a business card for our boutique gourmet fruit and vegetable food store using attached logo design, with the colour options of white, black and lime green. We would like it to be unique and classic, with a large image of the logo on the back of the business card, and the business card details plus a design on the front.

Target Market(s)

High income earners in an affluent Melbourne suburb who value high quality products and done mind paying for it

Industry/Entity Type

Retail

Contact Information for Business Card

Business name: Harwick's Fine Food Merchant
Address: 27 Plumtree Rd, Kelsby VIC 3158
Name: TBC
Position Title: Director
Phone Number: TBC
Mobile: TBC

Business name is: Harwick's Fine Food Merchant. Please allow space for us to fill in the business address, contact number, person's name, position Title and mobile number.

Colors
acd036

Requirements
Must have
• The logo must have our business logo on the back, and our business details and contact details on the front. It must include the colours of white, black and lime green
Nice to have
• It can have different background colours on the front and on the back.
Should not have
• It should not have any other colours aside from white, black and lime green

```html
<!DOCTYPE html>
<html lang="en">
<head>
<meta charset="utf-8">
<title>Harwick's Fine Food Merchant – Business Card</title>
<link rel="stylesheet" href="https://fonts.googleapis.com/css2?family=Josefin+Sans:wght@400;600&display=swap">
<style>
  :root {
    --lime: #acd036;
    --ink: #231f20;
    --paper: #ffffff;
  }
  html, body {
    margin: 0;
    padding: 0;
    overflow: hidden;
    background: var(--paper);
  }
  .card {
    position: relative;
    width: 1200px;
    height: 683px;
    background: var(--paper);
    overflow: hidden;
    font-family: "Josefin Sans", sans-serif;
    color: var(--ink);
  }
  .produce-column {
    position: absolute;
    top: 0;
    width: 196px;
    height: 683px;
    background: var(--lime);
  }
  .produce-column--left { left: 0; }
  .produce-column--right { right: 0; }
  .details {
    position: absolute;
    left: 196px;
    right: 196px;
    top: 0;
    height: 683px;
    text-align: center;
  }
  .business-name {
    position: absolute;
    left: 0;
    right: 0;
    top: 158px;
    margin: 0;
    font-size: 51px;
    font-weight: 400;
    line-height: 1;
    letter-spacing: 0.2px;
  }
  .divider {
    position: absolute;
    left: 37px;
    top: 249px;
  }
  .detail-line {
    position: absolute;
    left: 0;
    right: 0;
    margin: 0;
    font-size: 35px;
    font-weight: 400;
    line-height: 1;
  }
  .detail-line--address { top: 310px; }
  .detail-line--name { top: 378px; }
  .detail-line--role { top: 447px; }
  .detail-line--phone { top: 516px; }
</style>
</head>
<body>
  <div class="card">
    <div class="produce-column produce-column--left" role="img" aria-label="Line illustration of a carrot, an apple and a bottle stacked in lime green"></div>

    <div class="details">
      <h1 class="business-name">Harwick's Fine Food Merchant</h1>
      <svg class="divider" width="735" height="12" viewBox="0 0 735 12" aria-hidden="true">
        <line x1="3" y1="6" x2="732" y2="6" stroke="#acd036" stroke-width="5.5" stroke-linecap="round" stroke-dasharray="0 14.58"/>
      </svg>
      <p class="detail-line detail-line--address">27 Plumtree Rd, Kelsby VIC 3158</p>
      <p class="detail-line detail-line--name">Nadia Lorne</p>
      <p class="detail-line detail-line--role">Director</p>
      <p class="detail-line detail-line--phone">111-987-654</p>
    </div>

    <div class="produce-column produce-column--right" role="img" aria-label="Line illustration of a carrot, an apple and a bottle stacked in lime green"></div>
  </div>
</body>
</html>
```